Home inspection business! professional look attracting customers just by looks. Read must haves

its a new business I started on my own for home inspections I would like something very professional to give to real estate agents and clients, its going to have my license number on it my business phone number my name my website as well etc on the back side it will be servicing areas and also what kind of services I offer I also have a business card from someone else the way I would like mine to be. I will attach my logo

Home Inspection

listed in nice to haves

• phone number - 555 293 8471
• website- hollowpinecheck.com
• license number #2938475610
• my name Gavin keropulis
• picture of my logo and me on the front
• on the back of the card. stating I am servicing All of New York and Long Island
• also services I will offer will be home inspection -mold inspection -lead inspection -radon inspection -Termite Inspection -Infared Scan.
• and also we provide inspections for single family homes condos co-ops town-homes
• and commercial property
• same colors as the logos and also if you recommend fonts to look like the logo not sure up to you

```html
<!DOCTYPE html>
<html lang="en">
<head>
<meta charset="utf-8">
<title>Hollow Pine Check – Business Card</title>
<link rel="stylesheet" href="https://fonts.googleapis.com/css2?family=Montserrat:wght@500;600;700&family=Roboto:wght@400;500&display=swap">
<style>
  :root {
    --bg: #e6e6e6;
    --card-dark: #2a2a2b;
    --card-light: #ffffff;
    --brand-blue: #4a9ee0;
    --ink-grey: #555a60;
    --text-light: #d4d4d4;
    --white: #ffffff;
  }
  * { box-sizing: border-box; margin: 0; padding: 0; }
  html, body { width: 1200px; height: 900px; overflow: hidden; }
  body {
    background: var(--bg);
    font-family: "Roboto", Arial, sans-serif;
    position: relative;
  }
  .card {
    position: absolute;
    left: 250px;
    width: 700px;
    height: 400px;
    box-shadow: 0 6px 18px rgba(0,0,0,.18);
    overflow: hidden;
  }
  .card-back { top: 30px; background: var(--card-dark); color: var(--text-light); text-align: center; }
  .card-front { top: 470px; background: var(--card-light); }

  .brand { display: flex; align-items: center; gap: 14px; }
  .brand-dot { width: 34px; height: 34px; border-radius: 50%; background: var(--brand-blue); flex: none; }
  .brand-name {
    font-family: "Montserrat", Arial, sans-serif;
    font-weight: 700;
    font-size: 34px;
    letter-spacing: .5px;
    text-transform: uppercase;
    white-space: nowrap;
  }
  .card-back .brand { justify-content: center; margin-top: 92px; }
  .card-back .brand-name { color: var(--white); }

  .service-area {
    margin-top: 52px;
    font-family: "Montserrat", Arial, sans-serif;
    font-weight: 700;
    font-size: 16px;
    color: var(--brand-blue);
    text-transform: uppercase;
  }
  .service-list { margin-top: 12px; font-size: 16px; line-height: 1.3; }

  .card-front .brand { position: absolute; left: 36px; top: 178px; gap: 12px; }
  .card-front .brand-dot { width: 30px; height: 30px; }
  .card-front .brand-name { color: var(--ink-grey); font-size: 26px; }
  .divider { position: absolute; left: 410px; top: 62px; width: 2px; height: 140px; background: var(--brand-blue); }
  .contact { position: absolute; left: 430px; top: 60px; }
  .contact-name {
    font-family: "Montserrat", Arial, sans-serif;
    font-weight: 700;
    font-size: 24px;
    color: var(--brand-blue);
    margin-bottom: 8px;
    white-space: nowrap;
  }
  .contact-line { display: flex; align-items: center; gap: 8px; font-size: 16px; color: var(--ink-grey); line-height: 1.6; white-space: nowrap; }
  .contact-line svg { width: 14px; height: 14px; fill: var(--brand-blue); flex: none; }
  .swoosh { position: absolute; inset: 0; }
  .license {
    position: absolute; left: 40px; bottom: 16px;
    color: var(--white); font-size: 19px; letter-spacing: .5px;
  }
</style>
</head>
<body>
  <section class="card card-back">
    <div class="brand">
      <span class="brand-dot"></span>
      <span class="brand-name">Hollow Pine Check</span>
    </div>
    <p class="service-area">Stating I am servicing all of New York and Long Island</p>
    <p class="service-list">
      home inspection • mold inspection • lead inspection<br>
      radon inspection • Termite Inspection • Infared Scan<br>
      we provide inspections for single family homes condos co-ops town-homes<br>
      and commercial property
    </p>
  </section>

  <section class="card card-front">
    <svg class="swoosh" viewBox="0 0 700 400" preserveAspectRatio="none" aria-hidden="true">
      <path d="M0,400 L0,346 C210,284 460,284 700,222 L700,400 Z" fill="var(--brand-blue)"/>
      <path d="M0,400 L0,354 C212,294 465,294 700,240 L700,400 Z" fill="var(--white)"/>
      <path d="M0,400 L0,362 C215,302 470,302 700,252 L700,400 Z" fill="var(--card-dark)"/>
    </svg>
    <div class="brand">
      <span class="brand-dot"></span>
      <span class="brand-name">Hollow Pine Check</span>
    </div>
    <span class="divider"></span>
    <div class="contact">
      <p class="contact-name">Gavin keropulis</p>
      <p class="contact-line">
        <svg viewBox="0 0 24 24"><path d="M6.6 10.8a15.1 15.1 0 0 0 6.6 6.6l2.2-2.2a1 1 0 0 1 1-.25 11.4 11.4 0 0 0 3.6.57 1 1 0 0 1 1 1V20a1 1 0 0 1-1 1A17 17 0 0 1 3 4a1 1 0 0 1 1-1h3.5a1 1 0 0 1 1 1c0 1.25.2 2.45.57 3.57a1 1 0 0 1-.25 1z"/></svg>
        555 293 8471
      </p>
      <p class="contact-line">
        <svg viewBox="0 0 24 24"><path d="M2 5h20v14H2z M2 5l10 8 10-8" fill="none" stroke="var(--brand-blue)" stroke-width="2"/></svg>
        info@hollowpinecheck.com
      </p>
      <p class="contact-line">
        <svg viewBox="0 0 24 24"><circle cx="12" cy="12" r="10"/></svg>
        www.hollowpinecheck.com
      </p>
    </div>
    <p class="license">Lic #2938475610</p>
  </section>
</body>
</html>
```